Unique business card design

We are looking for a design that reflects our unique social media and online marketing agency "Kestrel Media". We are a young agency with a focus on speakers, coaches and trainers. In other words, we support people who want to do good with their work and help other people live a happier, more successful and fulfilling life, reach as many people as possible with their work and thus have an influence. Our values are: sustainability, creating added value, individuality, proactivity. We want our clients to feel comfortable with us and that's why the relationship with them is very important to us. We want every customer to become a lifelong friend of the company. Most of our clients are premium coaches, meaning they are in the higher priced segment and expect seriousness, professionalism and quality. All of these things should reflect our business card as well. I look forward to feedback. Best regards, Tomas Wylander

```html
<!DOCTYPE html>
<html lang="en">
<head>
<meta charset="utf-8">
<title>Kestrel Media – Business Card</title>
<link href="https://fonts.googleapis.com/css2?family=Roboto+Condensed:wght@400;700&display=swap" rel="stylesheet">
<style>
  :root {
    --brand-blue: #1570b8;
    --band-deep: #1f5fa3;
    --band-mid: #0e72bd;
    --band-dark: #233f7d;
    --ink-grey: #9aa3ab;
    --icon-grey: #a3abb3;
    --card-line: #3f86c6;
    --paper: #ffffff;
  }
  * { box-sizing: border-box; margin: 0; padding: 0; }
  html, body {
    width: 1200px; height: 1200px; overflow: hidden;
    background: var(--paper);
    font-family: "Roboto Condensed", "Arial Narrow", sans-serif;
  }
  .sheet { position: relative; width: 1200px; height: 1200px; }

  .card {
    position: absolute; left: 247px; width: 670px;
    background: var(--paper);
    border: 1px solid var(--card-line);
    overflow: hidden;
  }
  .card--front { top: 135px; height: 373px; }
  .card--back { top: 638px; height: 372px; }

  .facet-band {
    position: absolute; left: 0; width: 100%;
    background: linear-gradient(100deg, var(--band-mid) 0%, var(--band-deep) 35%, var(--band-dark) 55%, var(--band-deep) 72%, var(--band-mid) 100%);
  }
  .card--front .facet-band { top: 0; height: 186px; }
  .card--back .facet-band { bottom: 0; height: 83px; }

  .front-notch {
    position: absolute; left: 178px; top: 80px;
    width: 314px; height: 106px; background: var(--paper);
  }
  .front-brand {
    position: absolute; left: 178px; top: 80px; width: 314px; height: 190px;
    display: flex; align-items: center; justify-content: center; gap: 14px;
  }
  .front-brand .mark-square { width: 46px; height: 46px; background: var(--band-dark); }
  .front-brand .brand-name {
    font-size: 44px; font-weight: 400; color: var(--band-dark); letter-spacing: 0.5px;
  }

  .person {
    position: absolute; left: 66px; top: 62px; width: 258px; text-align: center;
  }
  .person-name {
    font-size: 27px; font-weight: 700; color: var(--brand-blue); letter-spacing: 0.6px;
  }
  .person-role {
    font-size: 17px; font-weight: 700; color: var(--ink-grey); letter-spacing: 0.5px; margin-top: 2px;
  }

  .back-brand {
    position: absolute; left: 67px; top: 160px;
    display: flex; align-items: center; gap: 8px;
  }
  .back-brand .mark-square { width: 26px; height: 26px; background: var(--band-dark); }
  .back-brand .brand-name { font-size: 24px; font-weight: 400; color: var(--band-dark); }

  .contacts { position: absolute; left: 355px; top: 54px; list-style: none; }
  .contact {
    display: flex; align-items: center; height: 30px; margin-bottom: 19px;
  }
  .contact-icon { width: 30px; height: 30px; flex: none; }
  .contact-text {
    margin-left: 10px; font-size: 18.5px; font-weight: 700; color: var(--brand-blue); letter-spacing: 0.4px;
  }
  .contact--web .contact-text { letter-spacing: 1.4px; }
</style>
</head>
<body>
<div class="sheet">

  <section class="card card--front">
    <div class="facet-band" role="img" aria-label="Angular faceted pattern in overlapping shades of blue"></div>
    <div class="front-notch"></div>
    <div class="front-brand">
      <span class="mark-square"></span>
      <span class="brand-name">Kestrel Media</span>
    </div>
  </section>

  <section class="card card--back">
    <div class="person">
      <h1 class="person-name">TOMAS WYLANDER</h1>
      <p class="person-role">marketing manager</p>
    </div>

    <div class="back-brand">
      <span class="mark-square"></span>
      <span class="brand-name">Kestrel Media</span>
    </div>

    <ul class="contacts">
      <li class="contact contact--phone">
        <svg class="contact-icon" viewBox="0 0 30 30" aria-hidden="true">
          <circle cx="15" cy="15" r="15" fill="var(--icon-grey)"/>
          <path d="M10.5 8.5c.6-.5 1.4-.4 1.8.2l1.3 2c.3.5.2 1.1-.2 1.5l-.9.8c.6 1.5 1.8 2.8 3.3 3.5l.8-.9c.4-.4 1-.5 1.5-.2l2 1.3c.6.4.7 1.2.2 1.8l-.9 1c-.8.8-2 1-3 .6-3.3-1.3-5.9-3.9-7.2-7.2-.4-1-.2-2.2.6-3z" fill="#fff"/>
        </svg>
        <span class="contact-text">+64 27 418 3062</span>
      </li>
      <li class="contact contact--address">
        <svg class="contact-icon" viewBox="0 0 30 30" aria-hidden="true">
          <circle cx="15" cy="15" r="15" fill="var(--icon-grey)"/>
          <path d="M15 7a5 5 0 0 0-5 5c0 3.8 5 10 5 10s5-6.2 5-10a5 5 0 0 0-5-5z" fill="#fff"/>
          <circle cx="15" cy="12" r="1.9" fill="var(--icon-grey)"/>
        </svg>
        <span class="contact-text">42 Kowhai Rd Taupo</span>
      </li>
      <li class="contact contact--email">
        <svg class="contact-icon" viewBox="0 0 30 30" aria-hidden="true">
          <circle cx="15" cy="15" r="15" fill="var(--icon-grey)"/>
          <text x="15" y="20" text-anchor="middle" font-family="Arial, sans-serif" font-size="15" fill="#fff">@</text>
        </svg>
        <span class="contact-text">kestrelmedia@gmail.com</span>
      </li>
      <li class="contact contact--web">
        <svg class="contact-icon" viewBox="0 0 30 30" aria-hidden="true">
          <circle cx="15" cy="15" r="15" fill="var(--icon-grey)"/>
          <circle cx="15" cy="15" r="7.5" fill="none" stroke="#fff" stroke-width="1.6"/>
          <ellipse cx="15" cy="15" rx="3.2" ry="7.5" fill="none" stroke="#fff" stroke-width="1.3"/>
          <line x1="7.5" y1="15" x2="22.5" y2="15" stroke="#fff" stroke-width="1.3"/>
        </svg>
        <span class="contact-text">www.kestrelmedia.com</span>
      </li>
    </ul>

    <div class="facet-band" role="img" aria-label="Angular faceted pattern in overlapping shades of blue"></div>
  </section>

</div>
</body>
</html>
```